BROCHURE VELMOTIX

I HAVE TO REORGANIZE THE ATTACHED BROCHURE

Target Market(s)

FACTORY USE

Industry/Entity Type

MEDICAL COSMETIC

Font styles to use
Serif

Colors
0054AA
0677BA
7BADD7
CADEEF
E8F1F8

Requirements
Must have
• I need only reorganize the brochure

```html
<!DOCTYPE html>
<html lang="it">
<head>
<meta charset="utf-8">
<title>VELMOTIX – Brochure</title>
<link href="https://fonts.googleapis.com/css2?family=Comfortaa:wght@400;600;700&family=Roboto:wght@400;500&display=swap" rel="stylesheet">
<style>
:root{
  --navy:#0054AA;
  --blue:#0677BA;
  --sky:#2aa3dc;
  --pale:#7BADD7;
  --mist:#CADEEF;
  --ice:#E8F1F8;
  --grey:#8c8c8c;
  --ink:#555;
  --sorter:#e9e9e9;
}
*{margin:0;padding:0;box-sizing:border-box}
html,body{width:1200px;height:636px;overflow:hidden;background:var(--sorter)}
body{position:relative;font-family:'Comfortaa',sans-serif}
.slide{position:absolute;width:376px;height:282px;background:#fff;border:1px solid #c8c8c8;overflow:hidden}
.slide-base{position:absolute;left:0;right:0;bottom:0;height:80px;background:linear-gradient(180deg,rgba(255,255,255,0) 0%,#e3e7ec 60%,#cfd5dc 100%)}
.slide-num{position:absolute;font:12px 'Roboto',sans-serif;color:#444}
.brand{position:absolute;right:8px;top:9px;display:flex;align-items:center;gap:3px;font-weight:700;font-size:9px;color:var(--navy)}
.brand i{width:7px;height:7px;border-radius:50%;background:var(--blue);display:block}
.footer{position:absolute;left:5px;bottom:3px;font-size:5px;color:var(--navy)}
.pnum{position:absolute;right:6px;bottom:3px;font-size:5px;color:#666}
.title{position:absolute;left:41px;color:var(--sky);font-size:17.5px;font-weight:600;line-height:1.25}
.rule{position:absolute;left:0;height:1.5px;background:var(--navy)}
.center{position:absolute;left:20px;right:20px;text-align:center}
.dark{color:var(--navy)}
.light{color:var(--sky)}
.arrow{position:absolute}
.fill{position:absolute}
ul.points{position:absolute;left:22px;right:16px;top:63px;list-style:none;font-size:12.5px;line-height:15.5px;color:var(--grey)}
ul.points li{position:relative;padding-left:16px;margin-bottom:2px}
ul.points li::before{content:"•";position:absolute;left:2px;color:#aaa}
ul.points .strong{color:#6f6f6f}
ul.points u{text-decoration:underline}
</style>
</head>
<body>

<!-- Slide 7 -->
<section class="slide" style="left:6px;top:5px">
  <div class="slide-base"></div>
  <div class="brand"><i></i>VELMOTIX</div>
  <h2 class="title" style="left:41px;top:25px;color:var(--sky)">IL CAPELLO – Quanto Cresce?</h2>
  <div class="rule" style="top:51px;width:243px"></div>
  <p style="position:absolute;left:20px;top:68px;font-size:16.5px;color:var(--navy);font-weight:600">Quanti capelli abbiamo in testa?</p>
  <svg class="arrow" style="left:33px;top:96px" width="42" height="18"><path d="M0 5h28V0l14 9-14 9v-5H0z" fill="var(--navy)"/></svg>
  <p style="position:absolute;left:80px;top:95px;font:15px 'Roboto',sans-serif;color:var(--grey)">circa <b style="font-weight:500">120.000-150.000</b></p>
  <p style="position:absolute;left:20px;top:124px;width:340px;font-size:16.5px;line-height:21px;color:var(--navy);font-weight:600">di questi circa 10.000 sono in fase di caduta</p>
  <svg class="arrow" style="left:33px;top:169px" width="42" height="18"><path d="M0 5h28V0l14 9-14 9v-5H0z" fill="var(--navy)"/></svg>
  <p style="position:absolute;left:80px;top:169px;font-size:14.5px;color:var(--grey)"><b style="font-family:'Roboto',sans-serif;font-weight:500">30/50</b> capelli al giorno che cadono</p>
  <div style="position:absolute;left:74px;top:210px;width:220px;height:48px;border:1px solid var(--navy);font:9.5px/12px 'Roboto',sans-serif;color:var(--navy);text-align:center;padding-top:4px">SI DIMEZZA LA QUANTITA' DI CAPELLI<br>ACCETTATA COME RIENTRANTE NELLA<br><span style="color:var(--sky)">"CADUTA NORMALE QUOTIDIANA"</span></div>
  <div class="fill" role="img" aria-label="Faccina pensierosa con punti interrogativi" style="left:305px;top:190px;width:66px;height:78px;border-radius:50%;background:radial-gradient(circle at 40% 35%,#ffe35a,#f5b400)"></div>
  <span class="footer">© VELMOTIX</span><span class="pnum">7</span>
</section>
<span class="slide-num" style="left:6px;top:292px">7</span>

<!-- Slide 8 -->
<section class="slide" style="left:411px;top:5px">
  <div class="slide-base"></div>
  <div class="brand"><i></i>VELMOTIX</div>
  <h2 class="title" style="top:26px">L'INTOSSINAZIONE cos'è?</h2>
  <div class="rule" style="top:52px;width:235px"></div>
  <ul class="points">
    <li>Un eccessivo accumulo di tossine</li>
    <li>Difficoltà del tessuto cutaneo a svolgere la sua funzione di organo emuntore.</li>
    <li class="strong">Le tossine provengono dalle stesse attività cellulari: son sostanze di rifiuto che il nostro organismo produce. Non riuscendo a liberarsene, lo congestionano.</li>
    <li><u>L'intossinazione determina invecchiamento precoce.</u></li>
    <li class="strong"><u>Un'intossinazione trascurata può provocare la perdita di capelli.</u></li>
  </ul>
  <span class="footer">© VELMOTIX</span><span class="pnum">8</span>
</section>
<span class="slide-num" style="left:411px;top:292px">8</span>

<!-- Slide 9 -->
<section class="slide" style="left:816px;top:5px">
  <div class="slide-base"></div>
  <div class="brand"><i></i>VELMOTIX</div>
  <p class="center dark" style="top:53px;font-size:15px;line-height:18px">In situazioni normali i capillari venosi e linfatici si occupano del drenaggio – espulsione - di questi scarti prodotti quotidianamente e raccolti negli spazi interstiziali cellulari.</p>
  <p class="center light" style="top:153px;font-size:15px;line-height:18px">Un accumulo continuo e mai smaltito di questi ROS determina nel lungo periodo il verificarsi di veri e propri</p>
  <p class="center light" style="top:220px;font-size:15px;font-weight:600;color:var(--blue)">auto-avvelenamenti.</p>
  <span class="footer">© VELMOTIX</span><span class="pnum">9</span>
</section>
<span class="slide-num" style="left:816px;top:292px">9</span>

<!-- Slide 10 -->
<section class="slide" style="left:6px;top:329px">
  <div class="slide-base"></div>
  <div class="brand"><i></i>VELMOTIX</div>
  <p class="center dark" style="top:52px;left:40px;right:40px;font-size:15.5px;line-height:19px">Possiamo immaginare tutto questo come un sistema di raccolta dei rifiuti che non funziona come dovrebbe: inizialmente si conferiscono i sacchi negli appositi spazi.</p>
  <p class="center light" style="top:182px;left:90px;right:90px;font-size:15.5px;line-height:19px">Ma se nessuno si preoccupa di rimuoverli le conseguenze sono evidenti!</p>
  <span class="footer">© VELMOTIX</span><span class="pnum">10</span>
</section>
<span class="slide-num" style="left:6px;top:615px">10</span>

<!-- Slide 11 -->
<section class="slide" style="left:411px;top:329px">
  <div class="slide-base"></div>
  <div class="brand"><i></i>VELMOTIX</div>
  <h2 class="title" style="top:25px;font-size:18.5px">L'INTOSSINAZIONE come<br>avvviene?</h2>
  <div class="rule" style="top:72px;width:236px"></div>
  <div class="fill" role="img" aria-label="Persona che getta un sacco nel cassonetto" style="left:78px;top:80px;width:82px;height:54px;border-radius:50%;background:linear-gradient(135deg,#7b8a6a,#9fd13a 60%,#c8d0c8)"></div>
  <div class="fill" role="img" aria-label="Fila di cassonetti metallici" style="left:207px;top:82px;width:114px;height:70px;border-radius:50%;background:linear-gradient(135deg,#8e9498,#c7ccd0 55%,#7d8a6e)"></div>
  <div class="fill" role="img" aria-label="Cassonetti circondati da rifiuti" style="left:200px;top:161px;width:121px;height:78px;border-radius:50%;background:linear-gradient(135deg,#6c7a5c,#9aa0a2 50%,#4d4d4d)"></div>
  <div class="fill" role="img" aria-label="Sacco della spazzatura nero" style="left:20px;top:138px;width:38px;height:68px;border-radius:45%;background:linear-gradient(160deg,#555,#222)"></div>
  <div class="fill" role="img" aria-label="Sacchetti colorati per la raccolta differenziata" style="left:66px;top:188px;width:75px;height:55px;border-radius:50%;background:linear-gradient(90deg,#e23a3a,#2fb6c9 50%,#e8e04a)"></div>
  <svg class="arrow" style="left:0;top:0" width="376" height="282">
    <g fill="none" stroke="var(--navy)" stroke-width="5">
      <path d="M141 102H196"/>
      <path d="M321 120C345 140 348 190 328 205"/>
      <path d="M55 155C90 155 100 175 75 188"/>
      <path d="M142 225H152V150"/>
    </g>
    <g fill="var(--navy)">
      <path d="M194 95l12 7-12 7z"/>
      <path d="M330 197l-11 13 16-1z"/>
      <path d="M80 182l-10 9 13 3z"/>
      <path d="M145 152l7-12 7 12z"/>
    </g>
  </svg>
  <span class="footer">© VELMOTIX</span><span class="pnum">11</span>
</section>
<span class="slide-num" style="left:411px;top:615px">11</span>

<!-- Slide 12 -->
<section class="slide" style="left:816px;top:329px">
  <div class="slide-base"></div>
  <div class="brand"><i></i>VELMOTIX</div>
  <p class="center light" style="top:35px;left:30px;right:80px;font-size:18.5px;line-height:22.5px">LE CONSEGUENZE SONO SVARIATE ANOMALIE RELATIVE AL CUOIO CAPELLUTO!!</p>
  <p class="center dark" style="top:141px;left:30px;right:80px;font-size:18.5px;line-height:22.5px">PER QUESTA RAGIONE SI DEVE SEMPRE REALIZZARE UN PRESHAMPOO IN BASE A QUANTO OSSERVO.</p>
  <div class="fill" role="img" aria-label="Personaggio a forma di capello in camice che alza il pollice" style="left:300px;top:35px;width:72px;height:243px;border-radius:40% 40% 30% 30%;background:linear-gradient(180deg,#8a4a2a,#5a2c16 60%,#f0a060)"></div>
  <span class="footer">© VELMOTIX</span><span class="pnum">12</span>
</section>
<span class="slide-num" style="left:816px;top:615px">12</span>

</body>
</html>
```